Drywall plastering business card design

Attached is my new logo and a picture of my current business card. I would like my new logo incorporated in to the business card and also my website which is:
www.kowhaibaywallcraftsolutions.co.nz
Industry/Entity Type
Business
Contact Information for Business Card
I would like a picture of my van and my new logo on my new business card. See attached files for pictures of my old business card, van picture and logo.
Colors
0555a3
ffffff
Requirements
Must have
- New logo, Van, contact info

```html
<!DOCTYPE html>
<html lang="en">
<head>
<meta charset="utf-8">
<title>Kowhai Bay Wallcraft Solutions – Business Card</title>
<link href="https://fonts.googleapis.com/css2?family=Arimo:ital,wght@0,400;0,700;1,700&display=swap" rel="stylesheet">
<style>
  :root {
    --brand-blue: #0a6fbd;
    --ink-dark: #3a3a3a;
    --ink-mid: #444444;
    --white: #ffffff;
    --silver-light: #f4f4f4;
    --silver-mid: #d9d9d9;
    --silver-dark: #b5b5b5;
  }
  html, body {
    margin: 0;
    padding: 0;
    width: 1200px;
    height: 897px;
    overflow: hidden;
    background: var(--white);
    font-family: "Arimo", Arial, sans-serif;
  }
  .canvas {
    position: relative;
    width: 1200px;
    height: 897px;
  }
  .business-card {
    position: absolute;
    left: 122px;
    top: 153px;
    width: 925px;
    height: 567px;
    overflow: hidden;
    background: linear-gradient(100deg,
      var(--silver-dark) 0%,
      var(--silver-light) 22%,
      var(--white) 40%,
      var(--silver-mid) 62%,
      var(--silver-light) 80%,
      var(--silver-dark) 100%);
    box-shadow: 0 2px 10px rgba(0,0,0,0.25);
  }
  .brand-lockup {
    position: absolute;
    left: 30px;
    top: 120px;
    width: 348px;
    display: flex;
    align-items: center;
    gap: 14px;
    justify-content: flex-end;
  }
  .brand-mark {
    width: 34px;
    height: 34px;
    flex: none;
    background: var(--brand-blue);
  }
  .brand-name {
    margin: 0;
    color: var(--brand-blue);
    font-weight: 700;
    font-size: 34px;
    line-height: 1.1;
    text-align: right;
  }
  .owner {
    position: absolute;
    right: 95px;
    top: 100px;
    text-align: right;
  }
  .owner-name {
    margin: 0;
    color: var(--ink-dark);
    font-weight: 700;
    font-size: 33px;
  }
  .owner-role {
    margin: 10px 0 0;
    color: var(--ink-mid);
    font-size: 26px;
  }
  .web-band {
    position: absolute;
    left: 386px;
    top: 204px;
    right: 0;
    height: 80px;
    background: var(--brand-blue);
    display: flex;
    align-items: center;
    padding-left: 14px;
    color: var(--white);
    font-weight: 700;
    font-size: 22px;
  }
  .contact-line {
    position: absolute;
    right: 95px;
    display: flex;
    align-items: center;
    gap: 8px;
    color: var(--ink-mid);
  }
  .contact-phone { top: 330px; font-size: 30px; }
  .contact-email { top: 385px; font-size: 26px; }
  .contact-line svg { fill: var(--brand-blue); }
  .tagline {
    position: absolute;
    right: 100px;
    top: 452px;
    margin: 0;
    color: var(--brand-blue);
    font-weight: 700;
    font-style: italic;
    font-size: 32px;
  }
</style>
</head>
<body>
<main class="canvas">
  <section class="business-card">
    <div class="brand-lockup">
      <span class="brand-mark"></span>
      <p class="brand-name">Kowhai Bay<br>Wallcraft<br>Solutions</p>
    </div>

    <div class="owner">
      <p class="owner-name">Mark Dunlow</p>
      <p class="owner-role">Proprietor</p>
    </div>

    <div class="web-band">www.kowhaibaywallcraftsolutions.co.nz</div>

    <div class="contact-line contact-phone">
      <svg width="22" height="28" viewBox="0 0 24 30" aria-hidden="true">
        <path d="M6 1 L10 8 L7 11 C8 16 11 20 15 22 L18 19 L24 24 L20 29 C10 28 2 18 1 6 Z"/>
      </svg>
      <span>027 555 01 42</span>
    </div>

    <div class="contact-line contact-email">
      <svg width="26" height="18" viewBox="0 0 26 18" aria-hidden="true">
        <rect x="1" y="1" width="24" height="16" fill="none" stroke="#0a6fbd" stroke-width="2"/>
        <path d="M1 1 L13 10 L25 1" fill="none" stroke="#0a6fbd" stroke-width="2"/>
      </svg>
      <span>kowhaibaywallcraft@mailbox.co.nz</span>
    </div>

    <p class="tagline">Large jobs or small - Always quality assured</p>
  </section>
</main>
</body>
</html>
```